The billboard should communicate confidence, energy and approachability while maintaining a professional, premium feel. Rather than relying on a standard agent photograph, property collage or crowded list of services, we would like an original creative idea that makes people look twice. This could involve a fun visual, clever headline, striking colour contrast or an unexpected real estate theme. The concept should feel positive and contemporary, with enough personality to become recognisable throughout the local community.

The key message should appeal to homeowners who are thinking about selling, preparing to sell or simply curious about the value of their property. Copy must be short, clear and conversational, supported by a direct call to action. The agent’s name, phone number and company branding should remain highly visible without competing with the main idea.

The finished billboard will measure 8.0 metres wide by 2.08 metres high (1224px x 324px), so the composition must suit a long landscape format. All important text and imagery should remain comfortably within safe margins and be legible from a distance. The design should avoid small writing, unnecessary detail and visual clutter.

The goal is to create a billboard that feels different from every other real estate sign in the area—something engaging, confident and easy to remember. It should build strong brand awareness, generate conversations and encourage local property owners to contact the agent when they are ready to make their next move. The concept should be adaptable for future campaigns, helping establish a consistent, distinctive and trusted local brand presence.

Target Market(s)

ages 30+

Industry/Entity Type

Real Estate

Requirements
Must have
• call Wade and phone number 0417 63 28 05
Nice to have
• Nice bright and yellow.. Exciting and grabbing

```html
<!DOCTYPE html>
<html lang="en">
<head>
<meta charset="utf-8">
<title>Lorne Bexley – Home Value Billboard</title>
<link rel="stylesheet" href="https://fonts.googleapis.com/css2?family=Lato:wght@400;700&family=Playfair+Display:wght@700&display=swap">
<style>
  :root {
    --brand-yellow: #ffe600;
    --band-grey: #5b5b5b;
    --ink: #4a4a4a;
    --paper: #ffffff;
    --stage: #2f2f2f;
  }
  * { margin: 0; padding: 0; box-sizing: border-box; }
  html, body {
    width: 1200px;
    height: 990px;
    overflow: hidden;
    background: var(--stage);
  }
  .stage {
    position: relative;
    width: 1200px;
    height: 990px;
  }
  .billboard {
    position: absolute;
    left: 50px;
    top: 349px;
    width: 1100px;
    height: 291px;
    background: var(--paper);
    box-shadow: 0 14px 40px rgba(0, 0, 0, 0.45);
    overflow: hidden;
  }
  .headline {
    position: absolute;
    left: 63px;
    top: 22px;
    font-family: "Playfair Display", Georgia, serif;
    font-weight: 700;
    font-size: 58px;
    line-height: 62px;
    letter-spacing: -0.5px;
    color: var(--ink);
    white-space: nowrap;
  }
  .headline .accent { color: var(--brand-yellow); }
  .info-band {
    position: absolute;
    left: 0;
    top: 171px;
    width: 866px;
    height: 120px;
    background: var(--band-grey);
  }
  .prompt-tag {
    position: absolute;
    left: 62px;
    top: 0;
    width: 378px;
    height: 52px;
    background: var(--brand-yellow);
    font-family: "Playfair Display", Georgia, serif;
    font-weight: 700;
    font-size: 30px;
    line-height: 52px;
    color: var(--ink);
    padding-left: 20px;
    white-space: nowrap;
  }
  .cta-rule {
    position: absolute;
    left: 440px;
    top: 51px;
    width: 426px;
    height: 1px;
    background: var(--brand-yellow);
    opacity: 0.8;
  }
  .cta {
    position: absolute;
    left: 482px;
    top: 14px;
    font-family: "Lato", Arial, sans-serif;
    font-weight: 700;
    font-size: 22px;
    color: var(--brand-yellow);
    white-space: nowrap;
  }
  .contact {
    position: absolute;
    top: 70px;
    font-family: "Lato", Arial, sans-serif;
    font-weight: 400;
    font-size: 20px;
    color: var(--paper);
    white-space: nowrap;
  }
  .contact.agent-name { left: 65px; }
  .contact.agent-phone { left: 482px; }
  .brand-panel {
    position: absolute;
    left: 866px;
    top: 0;
    width: 234px;
    height: 291px;
    display: flex;
    flex-direction: column;
    align-items: center;
    justify-content: center;
    gap: 28px;
  }
  .brand-name {
    display: flex;
    align-items: center;
    gap: 10px;
    font-family: "Lato", Arial, sans-serif;
    font-weight: 700;
    font-size: 22px;
    color: var(--ink);
    white-space: nowrap;
  }
  .brand-mark {
    width: 18px;
    height: 18px;
    background: var(--brand-yellow);
  }
  .web-address {
    font-family: "Lato", Arial, sans-serif;
    font-weight: 700;
    font-size: 11px;
    letter-spacing: 3px;
    color: var(--ink);
  }
</style>
</head>
<body>
<main class="stage">
  <section class="billboard" aria-label="Lorne Bexley home value billboard">
    <h1 class="headline">
      Your Home Might Be <span class="accent">Worth</span><br>
      <span class="accent">More</span> Than You Think.
    </h1>

    <div class="info-band">
      <p class="prompt-tag">Curious? Let’s find out.</p>
      <span class="cta-rule"></span>
      <p class="cta">DISCOVER YOUR HOME’S VALUE</p>
      <p class="contact agent-name">AGENT NAME</p>
      <p class="contact agent-phone">PHONE NUMBER</p>
    </div>

    <div class="brand-panel">
      <p class="brand-name"><span class="brand-mark"></span>Lorne Bexley</p>
      <p class="web-address">LORNEBEXLEY.COM</p>
    </div>
  </section>
</main>
</body>
</html>
```